New Alcoholic Spiked Seltzer Line

We need a can design for a line of low calorie alcoholic seltzer. This product is a sparkling water and vodka drink with no sugar added in a slim 12 oz can.

This is a lighter, healthier, alternative to the sugary ready-to-drinks on the market. The product contains only 3 ingredients: Vodka, Water and Natural Flavors. It has only 100 calories but still has 5% alcohol, so you don't need to sacrifice alcohol to cut calories.

This product also does not contain any preservatives.

We want this design to communicate the following objectives to the consumer and in this order:

1. Appetizing product
2.Low calorie
3.Communicate the type of beverage (Spiked Seltzer)

The brand name of the product is VELKA.

The flavor of the product needed to be used for the design is Mango-Orange.

Comparable products are:

www.brisavelfizz.example/
https://www.tarnowbubble.example
https://quellrind.example/

The designs should not infringe or copy the creative directions of the products mentionned above. They are only given so that you can better understand the type of product we are developing.

Target Market(s)

Young Professional women between the ages of 25 and 44

Industry/Entity Type

Product

Colors

Designer to choose colors to be used in the design.

Requirements
Must have
• Design extendibility, meaning it can be adapted for other flavors.
• This is a new category in the market we are targeting, so consumers must easily be able to identify what type of product this is.

```html
<!DOCTYPE html>
<html lang="en">
<head>
<meta charset="utf-8">
<title>VELKA Spiked Seltzer – Can Range</title>
<link href="https://fonts.googleapis.com/css2?family=Amatic+SC:wght@700&family=Josefin+Sans:wght@300;400&display=swap" rel="stylesheet">
<style>
  :root {
    --backdrop: #e6e6e6;
    --metal-light: #f2f4f6;
    --metal-mid: #d9dde2;
    --metal-dark: #b9bfc6;
    --ink: #1c1a1b;
    --paper: #ffffff;
    --watermelon: #f86e7c;
    --mango: #f8e21a;
    --cranberry: #d36af0;
  }
  * { box-sizing: border-box; margin: 0; padding: 0; }
  html, body {
    width: 1200px; height: 1200px; overflow: hidden;
    background: var(--backdrop);
  }
  .range {
    position: relative; width: 1200px; height: 1200px;
    display: flex; justify-content: center; align-items: center; gap: 50px;
  }
  .can-wrap {
    position: relative; width: 300px; height: 760px;
    background: linear-gradient(90deg, var(--metal-dark) 0%, var(--metal-light) 18%, var(--metal-mid) 55%, var(--metal-light) 80%, var(--metal-dark) 100%);
    overflow: hidden;
  }
  .flavour-splash {
    position: absolute; left: 60px; top: 20px; width: 200px; height: 720px;
    border-radius: 40px;
    opacity: .92;
  }
  .can-wrap--watermelon .flavour-splash { background: var(--watermelon); }
  .can-wrap--mango .flavour-splash { background: var(--mango); }
  .can-wrap--cranberry .flavour-splash { background: var(--cranberry); }
  .brand-mark {
    position: absolute; left: 50%; top: 150px; transform: translateX(-50%);
    width: 190px; height: 190px; border-radius: 50%;
    background: var(--ink);
    display: flex; align-items: center; justify-content: center;
  }
  .brand-name {
    font-family: "Josefin Sans", sans-serif; font-weight: 300;
    font-size: 50px; letter-spacing: 2px; color: var(--paper);
    padding-top: 8px;
  }
  .product-type {
    position: absolute; left: 0; right: 0; top: 360px; text-align: center;
    font-family: "Josefin Sans", sans-serif; font-weight: 400;
    font-size: 24px; letter-spacing: 2px; color: var(--ink);
  }
  .flavour-band {
    position: absolute; left: 30px; right: 30px; top: 440px; height: 58px;
    background: var(--ink);
    display: flex; align-items: center; justify-content: center;
    font-family: "Amatic SC", sans-serif; font-weight: 700;
    font-size: 40px; letter-spacing: 2px; color: var(--paper);
  }
  .claim-strip {
    position: absolute; left: 0; right: 0; bottom: 90px; height: 44px;
    background: var(--ink);
    display: flex; align-items: center; justify-content: space-around;
    font-family: "Josefin Sans", sans-serif; font-weight: 400;
    font-size: 17px; letter-spacing: .5px; color: var(--paper);
    white-space: nowrap;
  }
</style>
</head>
<body>
<main class="range">
  <section class="can-wrap can-wrap--watermelon">
    <div class="flavour-splash" role="img" aria-label="Watermelon-pink paint splash artwork"></div>
    <div class="brand-mark"><span class="brand-name">VELKA</span></div>
    <p class="product-type">SPIKED SELTZER</p>
    <p class="flavour-band">Watermelon</p>
    <p class="claim-strip"><span>LOW CALORIE</span><span>LOW CALORIE</span></p>
  </section>
  <section class="can-wrap can-wrap--mango">
    <div class="flavour-splash" role="img" aria-label="Mango-yellow paint splash artwork"></div>
    <div class="brand-mark"><span class="brand-name">VELKA</span></div>
    <p class="product-type">SPIKED SELTZER</p>
    <p class="flavour-band">Mango &amp; Orange</p>
    <p class="claim-strip"><span>LOW CALORIE</span><span>LOW CALORIE</span></p>
  </section>
  <section class="can-wrap can-wrap--cranberry">
    <div class="flavour-splash" role="img" aria-label="Cranberry-violet paint splash artwork"></div>
    <div class="brand-mark"><span class="brand-name">VELKA</span></div>
    <p class="product-type">SPIKED SELTZER</p>
    <p class="flavour-band">Cranberry &amp; Lime</p>
    <p class="claim-strip"><span>LOW CALORIE</span><span>LOW CALORIE</span></p>
  </section>
</main>
</body>
</html>
```